Industry automation wholesale website

www.velnora.eu provides solutions for automation, building automation and digital signage.

Our products are rugged, reliable, energy saving and representative.

Scope of pages:
● welcome page
- scope of products
- applications, success stories and news
● category page
- short introduction
- sub categories
- product highlights
● product page
- short introduction
- about 3 to 4 pictures
- technical specifications: materials, dimensions
- price
- related products

Optional:
● contact page
- address
- contact form
● blog
- picture
- text
● logo
● favicon / apple touch icon

Conclusion:
● We need a professionally looking site
● Bright colors (e.g. white, grey, metalic colors, blue)

some pages we like:
http://www.rubaskel.de/
http://www.parowind.de/

Target Market(s)

Our target market is the industrial sector
● Target audience: engineering and IT professionals

Industry/Entity Type

Building

Requirements
Must have
• ● only use free available fonts e.g. Lumivo Type Library (http://www.lumivotype.com/library)
Should not have
• ● sound
● flash

```html
<!DOCTYPE html>
<html lang="en">
<head>
<meta charset="utf-8">
<title>Velnora – Industrial Automation</title>
<link href="https://fonts.googleapis.com/css2?family=Source+Sans+3:wght@300;400;600;700&display=swap" rel="stylesheet">
<style>
:root{
  --brand:#1f6f96;
  --brand-dark:#1c6184;
  --button:#23729a;
  --ink:#2a2a2a;
  --body:#555;
  --hero-a:#9fb7b6;
  --hero-b:#7f9a9b;
  --footer:#2c6b8a;
  --footer-deep:#245d79;
  --field:#a8e0f5;
  --news:#8fd9f7;
  --bottom:#11232d;
  --white:#fff;
}
*{box-sizing:border-box;margin:0;padding:0}
html,body{width:1053px;height:1200px;overflow:hidden}
body{font-family:"Source Sans 3",sans-serif;background:var(--white);color:var(--ink);position:relative}
.abs{position:absolute}

/* header */
.brand{left:207px;top:14px;display:flex;align-items:center;gap:10px}
.brand-name{font-size:52px;font-weight:400;color:var(--brand);letter-spacing:1px;line-height:1}
.brand-dot{width:14px;height:14px;border-radius:50%;background:var(--brand)}
.contact-line{top:20px;font-size:12px;font-weight:700;color:var(--ink);display:flex;align-items:center;gap:8px}
.contact-mail{left:640px}
.contact-phone{left:760px}
.search{left:639px;top:51px;width:225px;height:23px;border:1px solid #bbb;font-size:11px;color:#444;padding:4px 7px;display:flex;justify-content:space-between;align-items:center}
.nav{left:207px;top:93px;display:flex;align-items:center;font-size:12px;color:var(--ink)}
.nav-home{background:var(--button);color:var(--white);width:64px;height:29px;display:flex;align-items:center;justify-content:center;margin-right:18px}
.nav-item{padding:0 18px}
.nav-sep{color:#444}
.lang{left:762px;top:101px;font-size:12px;color:#333;display:flex;align-items:center;gap:8px}

/* hero */
.hero{left:0;top:142px;width:1053px;height:381px;background:linear-gradient(180deg,var(--hero-a),var(--hero-b))}
.hero-products{left:600px;top:222px;width:245px;height:275px;background:linear-gradient(135deg,#3d4a52,#5b88a8 55%,#2e3a42);opacity:.85;border-radius:6px}
.hero-title{left:208px;top:240px;font-size:34px;font-weight:400;color:#1d1d1d;line-height:1;white-space:nowrap}
.hero-title b{color:var(--brand-dark);font-weight:700}
.hero-sub{left:208px;top:275px;font-size:21px;font-weight:300;color:#3d4548;line-height:24px;width:370px}
.hero-btn{left:209px;top:415px;width:96px;height:34px;background:#236f8c;color:var(--white);font-size:15px;display:flex;align-items:center;justify-content:center;border-radius:3px}

/* features */
.feature{top:553px;width:191px}
.feature h2{font-size:15px;font-weight:600;color:var(--brand);line-height:16px;height:41px}
.feature-image{width:191px;height:128px}
.feature p{margin-top:16px;font-size:9px;line-height:13.2px;color:var(--body);text-align:justify;height:140px}
.more{display:flex;align-items:center;gap:11px;font-size:10.5px;color:#444}
.more-icon{width:20px;height:20px;border-radius:50%;background:var(--brand-dark);display:flex;align-items:center;justify-content:center}
.col1{left:207px}.col2{left:439px}.col3{left:673px}

/* footer */
.footer{left:0;top:937px;width:1053px;height:231px;background:linear-gradient(180deg,var(--footer),var(--footer-deep))}
.footer-heading{font-size:14px;font-weight:400;color:var(--white);line-height:18px}
.links{left:207px;top:952px}
.links ul{list-style:none;margin-top:9px}
.links li{font-size:10px;color:var(--white);line-height:15.8px}
.form{left:439px;top:952px;width:190px}
.field{background:var(--field);font-size:10px;color:#264b5c;padding:6px 7px;height:25px}
.row{display:flex;gap:7px;margin-top:9px}
.row .field{width:92px}
.email{margin-top:7px}
.message{margin-top:7px;height:55px}
.send{margin:14px auto 0;width:86px;height:25px;background:#d9f1fb;color:#1f5f7e;font-size:10px;font-weight:700;display:flex;align-items:center;justify-content:center;border-radius:2px}
.news{left:673px;top:952px;width:190px}
.news-item{margin-top:9px}
.news-item + .news-item{margin-top:20px}
.news-item h4{font-size:10.5px;font-weight:400;color:var(--news)}
.news-item p{font-size:9.5px;color:var(--white);line-height:12px;text-align:justify}
.bottom{left:0;top:1168px;width:1053px;height:32px;background:var(--bottom);color:var(--white);font-size:9.5px;font-weight:700;display:flex;align-items:center;justify-content:center}
</style>
</head>
<body>

<header>
  <div class="abs brand"><span class="brand-name">velnora</span><span class="brand-dot"></span></div>
  <div class="abs contact-line contact-mail">
    <svg width="18" height="12" viewBox="0 0 18 12"><rect x="0.5" y="0.5" width="17" height="11" fill="#2a6a8d"/><path d="M1 1l8 6 8-6" stroke="#fff" stroke-width="1" fill="none"/></svg>
    info@velnora.de
  </div>
  <div class="abs contact-line contact-phone">
    <svg width="18" height="15" viewBox="0 0 18 15"><path d="M1 5c0-3 16-3 16 0v2h-4V5H5v2H1z" fill="#2a6a8d"/><rect x="4" y="7" width="10" height="7" rx="1" fill="#2a6a8d"/><circle cx="9" cy="10.5" r="2" fill="#fff"/></svg>
    +49-211-5520914
  </div>
  <div class="abs search"><span>Search Product</span>
    <svg width="14" height="14" viewBox="0 0 14 14"><circle cx="5.5" cy="5.5" r="4.5" stroke="#7aa" stroke-width="1.3" fill="none"/><path d="M9 9l4 4" stroke="#7aa" stroke-width="1.5"/></svg>
  </div>
  <nav class="abs nav">
    <span class="nav-home">Home</span>
    <span class="nav-item">Products</span><span class="nav-sep">|</span>
    <span class="nav-item">Contact</span><span class="nav-sep">|</span>
    <span class="nav-item">search</span><span class="nav-sep">|</span>
    <span class="nav-item">Shopping cart</span>
  </nav>
  <div class="abs lang">-Select Language-
    <svg width="9" height="6" viewBox="0 0 9 6"><path d="M0 0h9L4.5 6z" fill="#2a6a8d"/></svg>
  </div>
</header>

<section>
  <div class="abs hero" role="img" aria-label="Industrial plant skyline at dusk in muted teal tones"></div>
  <div class="abs hero-products" role="img" aria-label="Two industrial touch panel computers"></div>
  <h1 class="abs hero-title"><b>Velnora</b> provides solutions</h1>
  <p class="abs hero-sub">for automationbuilding automation and digital signage.</p>
  <a class="abs hero-btn">Read more</a>
</section>

<main>
  <article class="abs feature col1">
    <h2>Modbus RTU / RS485 Remote IO Modules</h2>
    <div class="feature-image" role="img" aria-label="Rack of industrial computers and IO modules" style="background:linear-gradient(135deg,#e8eef2,#8a97a3 60%,#3b4650)"></div>
    <p>RS485 Remote IO modules are ideal to realize decentralized distributed IO units over long distances. We provide the whole product range form Remote IO Modules with RS485 Bus and Modbus RTU such as analogue IO Modules, digital IO Modules, Relay Modules and Timer / Counter Modules. Also we provide RS422 and RS485 converter to RS232, USB, TCP/IP.</p>
    <div class="more"><span class="more-icon"><svg width="8" height="8" viewBox="0 0 8 8"><path d="M2 1l3 3-3 3" stroke="#fff" stroke-width="1.3" fill="none"/></svg></span>Read more</div>
  </article>

  <article class="abs feature col2">
    <h2>Toch Panal Industrial Computer</h2>
    <div class="feature-image" role="img" aria-label="Touch panel computers with a hand touching the screen" style="background:linear-gradient(135deg,#f2f3f4,#9aa0a6 55%,#4a5056)"></div>
    <p>Velnora provide prestigious Touch Panel Computer for your building automation. Also we provide Human Machine Interfaces for e.g. shopping malls, hotels or hospitals. KorvexDAQ Industry Computer are also used e.g. as POS-terminal, for home automation or surveillance systems. Building automation is a huge field where we can provide individual solutions - do not hesitate to get in touch - call us at +49 211 552 09 14.</p>
    <div class="more"><span class="more-icon"><svg width="8" height="8" viewBox="0 0 8 8"><path d="M2 1l3 3-3 3" stroke="#fff" stroke-width="1.3" fill="none"/></svg></span>Read more</div>
  </article>

  <article class="abs feature col3">
    <h2>Embedded System&nbsp; for industrial automation</h2>
    <div class="feature-image" role="img" aria-label="Compact embedded computer resting on an open hand with white wings" style="background:linear-gradient(180deg,#f4f6f7,#d9dde0 45%,#2b2f33 60%,#c9a38a 85%)"></div>
    <p>Velnora is your specialist partner for industrial automation. We at Velnora provide individual solutions for unitized measurement and offer the whole range of products, from interface converter over RS-485 Embedded Systems and powerful Panel-PCs. The Taiwanese specialist with the trademark KORVEX is one of the leading manufacturers of reliable industrial hardware for unitized instrumentation control and automation.</p>
    <div class="more"><span class="more-icon"><svg width="8" height="8" viewBox="0 0 8 8"><path d="M2 1l3 3-3 3" stroke="#fff" stroke-width="1.3" fill="none"/></svg></span>Read more</div>
  </article>
</main>

<footer>
  <div class="abs footer"></div>
  <div class="abs links">
    <h3 class="footer-heading">Quick Links</h3>
    <ul>
      <li>Home</li><li>About us</li><li>Products</li><li>Shoping Carts</li>
      <li>Terms of use</li><li>Privacy policy</li><li>Customer Support</li>
    </ul>
  </div>
  <div class="abs form">
    <h3 class="footer-heading">Contact us</h3>
    <div class="row"><div class="field">Name</div><div class="field">Ph no.</div></div>
    <div class="field email">Email Address</div>
    <div class="field message">Message :</div>
    <div class="send">SEND MESSAGE</div>
  </div>
  <div class="abs news">
    <h3 class="footer-heading">Lates News</h3>
    <div class="news-item"><h4>News Headline Goes Here</h4><p>Covenant waiver verlängert, erste Überprüfung am 30. September 2014</p></div>
    <div class="news-item"><h4>News Headline Goes Here</h4><p>Covenant waiver verlängert, erste Überprüfung am 30. September 2014</p></div>
    <div class="news-item"><h4>News Headline Goes Here</h4><p>Covenant waiver verlängert, erste Überprüfung am 30. September 2014</p></div>
  </div>
  <div class="abs bottom">copyright © 2013. All rights reserved.</div>
</footer>

</body>
</html>
```